Website design for a hair building fibre

Hi I’m needing a website made for both men and women to purchase the product is a hair building fibre that you apply to thinning hair to make your hair look really thick I’ll need the website to be easy to use professional and also very classy I will need it to work with later fund quo bank and credit cards I’ll need to have the CEO words and everything ready so I can sell I don’t have photos that I want to put on there so I’ll need a website designer to assist me in having the beautiful photos on there I know very little about websites so I need someone to be able to do it all for me

I can only provide photos of the colours of the products
I believe there will be 8 colours to sell as well
I’ve uploaded a photo of the logo I’d really like it if the website designer can check other competitors website so my website does not look like theres, I don’t want my website to look like a copied website of the competitors I’m located in Australia.
I’m also looking for someone who can open up a Chatterfold and Glimoravo page and then can unload photos on them ready for consumers to view and buy.

```html
<!DOCTYPE html>
<html lang="en">
<head>
<meta charset="utf-8">
<title>Mille Strand – Hair Building Fibre</title>
<link href="https://fonts.googleapis.com/css2?family=Montserrat:wght@300;400;500;600;700;800&display=swap" rel="stylesheet">
<style>
:root{
  --bg:#0a131e;
  --bg-panel:#0f1b29;
  --header:#0d1826;
  --accent:#6dd3f2;
  --accent-dark:#0a1a28;
  --line:#2b3849;
  --text:#ffffff;
  --muted:#c9d3dd;
  --tag-new:#e3173e;
  --tag-sale:#e3c51b;
  --tag-sale2:#1fb48a;
}
*{margin:0;padding:0;box-sizing:border-box}
html,body{width:1200px;height:3363px;overflow:hidden}
body{background:var(--bg);color:var(--text);font-family:"Montserrat",sans-serif;position:relative}
.abs{position:absolute}

/* header */
.site-header{position:absolute;left:0;top:0;width:1200px;height:112px;background:var(--header)}
.brand{position:absolute;left:146px;top:38px;font-size:38px;font-weight:300;color:var(--accent);letter-spacing:1px}
.search{position:absolute;left:763px;top:13px;width:236px;height:39px;display:flex}
.search-field{flex:1;background:#fff;font-size:11px;color:#666;padding:13px 20px}
.search-btn{width:39px;background:var(--accent);display:flex;align-items:center;justify-content:center}
.cart{position:absolute;left:1014px;top:16px}
.main-nav{position:absolute;right:147px;top:75px;display:flex;gap:41px;font-size:15px;font-weight:500}
.main-nav a{color:var(--text);text-decoration:none}

/* hero */
.hero{position:absolute;left:0;top:112px;width:1200px;height:560px}
.hero-title{position:absolute;left:628px;top:190px;font-size:56px;font-weight:800;line-height:62px}
.hero-sub{position:absolute;left:632px;top:330px;font-size:19px;font-weight:700;line-height:30px;width:440px}
.btn{position:absolute;background:var(--accent);color:var(--accent-dark);font-weight:700;border-radius:30px;display:flex;align-items:center;justify-content:center;text-decoration:none}
.btn-lg{font-size:16px}
.btn-sm{font-size:12px;width:126px;height:45px}
.slider-dot{position:absolute;left:1139px;width:13px;height:13px;border-radius:50%;background:#fff}
.slider-dot.is-active{background:var(--accent)}

/* sections */
.section-title{position:absolute;left:0;width:1200px;text-align:center;font-weight:800;font-size:44px}

.product-card{position:absolute;width:211px;height:256px;border:1px solid var(--line)}
.product-shot{position:absolute;left:68px;top:22px;width:74px;height:212px;border-radius:14px 14px 8px 8px;background:linear-gradient(180deg,#1b1b1b 0 26%,#d9dadc 26% 100%)}
.tag{position:absolute;right:12px;top:15px;font-size:11px;font-weight:800;padding:3px 5px;color:#fff}
.tag-new{background:var(--tag-new)}
.tag-sale{background:var(--tag-sale)}
.tag-sale2{background:var(--tag-sale2)}
.product-name{position:absolute;width:211px;text-align:center;font-weight:700;font-size:17px}
.swatches{position:absolute;width:211px;display:flex;justify-content:center;gap:6px}
.sw{width:18px;height:18px;border-radius:50%}
.sw.is-selected{box-shadow:0 0 0 2px var(--bg),0 0 0 4px var(--accent)}
.c1{background:linear-gradient(135deg,#f6c46a,#c98a2a)}
.c2{background:linear-gradient(135deg,#b8663a,#6b3217)}
.c3{background:#f3ead4}
.c4{background:#9b3a1c}
.c5{background:#4a0f1a}
.c6{background:linear-gradient(135deg,#f7a46b,#c7643a)}
.c7{background:linear-gradient(135deg,#7fd3b8,#e48aa0)}
.c8{background:linear-gradient(135deg,#a34ac9,#5a1a7a)}

/* colours band */
.colours-band{position:absolute;left:0;top:1809px;width:600px;height:320px;background:var(--bg-panel)}
.colours-title{position:absolute;left:145px;top:1838px;font-size:42px;font-weight:800}
.colours-text{position:absolute;left:145px;top:1900px;width:400px;font-size:12.5px;line-height:25.5px;color:var(--muted)}
.colours-photo{position:absolute;left:600px;top:1809px;width:600px;height:320px;background:linear-gradient(90deg,#7fa8d8,#c23c8e 20%,#e4652b 35%,#c9a7c6 50%,#d8336f 62%,#f2a14b 75%,#c978d6 90%,#e79bc0)}

/* blog */
.blog-city{position:absolute;left:0;top:2827px;width:1200px;height:536px;background:linear-gradient(180deg,#1a2433 0%,#0f1a26 40%,#0a131e 100%)}
.blog-grid{position:absolute;left:144px;top:2338px;width:913px;height:489px;border:1px solid #8a96a3;display:grid;grid-template-columns:1fr 1fr 1fr;background:var(--bg)}
.blog-card{position:relative;border-right:1px solid #8a96a3;text-align:center;padding:0 28px}
.blog-card:last-child{border-right:none}
.blog-title{font-size:15px;font-weight:500;margin-top:52px}
.blog-date{font-size:12px;color:var(--accent);margin-top:14px}
.blog-text{font-size:11.5px;line-height:22.4px;color:var(--muted);margin-top:12px;text-align:justify;text-align-last:center}
.blog-card .btn{position:static;margin:38px auto 0}
.blog-card.is-short .blog-title{margin-top:32px}
.blog-card.is-short .btn{margin-top:18px}
.blog-photo{position:absolute;left:0;bottom:0;width:100%;height:245px;background:linear-gradient(90deg,#b9a690,#7b6a58 45%,#e0608f 52%,#c4436f)}

/* footer */
.footer-nav{position:absolute;left:143px;top:3178px;display:flex;gap:41px;font-size:15px;font-weight:500}
.footer-nav a{color:var(--text);text-decoration:none}
.copyright{position:absolute;left:143px;top:3229px;font-size:11px}
.footer-brand{position:absolute;left:739px;top:3180px;font-size:52px;font-weight:300;color:var(--accent);letter-spacing:1px}
.payments{position:absolute;left:143px;top:3283px;display:flex;gap:8px}
.pay{width:34px;height:22px;background:#eef2f6;color:#1c3f7a;font-size:7px;font-weight:700;display:flex;align-items:center;justify-content:center;border-radius:2px}
</style>
</head>
<body>

<header class="site-header">
  <div class="brand">MILLE STRAND</div>
  <div class="search">
    <div class="search-field">Search</div>
    <div class="search-btn">
      <svg width="14" height="14" viewBox="0 0 14 14"><circle cx="6" cy="6" r="4" fill="none" stroke="#fff" stroke-width="2"/><line x1="9" y1="9" x2="12.5" y2="12.5" stroke="#fff" stroke-width="2"/></svg>
    </div>
  </div>
  <svg class="cart" width="40" height="34" viewBox="0 0 40 34">
    <path d="M2 6h6l5 17h18l4-12H11" fill="none" stroke="#fff" stroke-width="1.6"/>
    <circle cx="15" cy="28" r="2.5" fill="none" stroke="#fff" stroke-width="1.4"/>
    <circle cx="28" cy="28" r="2.5" fill="none" stroke="#fff" stroke-width="1.4"/>
    <circle cx="32" cy="7" r="5" fill="none" stroke="#fff" stroke-width="1.4"/>
    <path d="M32 4.5v5M29.5 7h5" stroke="#fff" stroke-width="1.4"/>
  </svg>
  <nav class="main-nav">
    <a href="#">HOME</a><a href="#">ABOUT</a><a href="#">PRODUCTS</a><a href="#">NEWS</a><a href="#">BLOG</a><a href="#">CONTACT</a>
  </nav>
</header>

<section class="hero">
  <svg class="abs" width="1200" height="560" viewBox="0 0 1200 560" style="left:0;top:0">
    <defs>
      <linearGradient id="heroPhoto" x1="0" y1="0" x2="1" y2="1">
        <stop offset="0" stop-color="#dadada"/><stop offset="0.5" stop-color="#8a8a8a"/><stop offset="1" stop-color="#3a3a3a"/>
      </linearGradient>
    </defs>
    <path role="img" aria-label="Black and white photo of a woman with long straight dark hair" d="M0 0H522C480 120 560 200 582 330C600 440 520 540 380 552C250 560 110 520 0 480Z" fill="url(#heroPhoto)"/>
    <path d="M525 0C484 120 566 200 588 330C606 440 526 545 380 556" fill="none" stroke="var(--accent)" stroke-width="12"/>
    <path d="M0 478C120 548 300 575 440 520C565 468 620 420 760 420C910 420 1060 445 1200 462" fill="none" stroke="var(--accent)" stroke-width="12"/>
  </svg>
  <h1 class="hero-title" style="top:78px">HAIR BUILDING<br>FIBRE</h1>
  <p class="hero-sub" style="top:218px">Lorem ipsum doloametconsecdipiscing elit, sed do eiusmod tempor incididunt</p>
  <a class="btn btn-lg" href="#" style="left:632px;top:302px;width:165px;height:59px">SHOP NOW</a>
  <span class="slider-dot" style="top:195px"></span>
  <span class="slider-dot is-active" style="top:219px"></span>
  <span class="slider-dot" style="top:242px"></span>
</section>

<h2 class="section-title" style="top:742px">FEATURED PRODUCTS</h2>

<!-- product row 1 -->
<div class="product-card" style="left:143px;top:846px"><div class="product-shot" role="img" aria-label="Hair fibre canister, golden blonde"></div><span class="tag tag-new">NEW</span></div>
<div class="product-card" style="left:377px;top:846px"><div class="product-shot" role="img" aria-label="Hair fibre canister, light brown"></div></div>
<div class="product-card" style="left:611px;top:846px"><div class="product-shot" role="img" aria-label="Hair fibre canister, platinum blonde"></div><span class="tag tag-sale">SALE</span></div>
<div class="product-card" style="left:846px;top:846px"><div class="product-shot" role="img" aria-label="Hair fibre canister, auburn"></div></div>

<div class="product-name" style="left:143px;top:1129px">PRODUCT NAME</div>
<div class="product-name" style="left:377px;top:1129px">PRODUCT NAME</div>
<div class="product-name" style="left:611px;top:1129px">PRODUCT NAME</div>
<div class="product-name" style="left:846px;top:1129px">PRODUCT NAME</div>

<div class="swatches" style="left:143px;top:1166px"><i class="sw c1 is-selected"></i><i class="sw c2"></i><i class="sw c3"></i><i class="sw c4"></i><i class="sw c5"></i><i class="sw c6"></i><i class="sw c7"></i><i class="sw c8"></i></div>
<div class="swatches" style="left:377px;top:1166px"><i class="sw c1"></i><i class="sw c2 is-selected"></i><i class="sw c3"></i><i class="sw c4"></i><i class="sw c5"></i><i class="sw c6"></i><i class="sw c7"></i><i class="sw c8"></i></div>
<div class="swatches" style="left:611px;top:1166px"><i class="sw c1"></i><i class="sw c2"></i><i class="sw c3 is-selected"></i><i class="sw c4"></i><i class="sw c5"></i><i class="sw c6"></i><i class="sw c7"></i><i class="sw c8"></i></div>
<div class="swatches" style="left:846px;top:1166px"><i class="sw c1"></i><i class="sw c2"></i><i class="sw c3"></i><i class="sw c4 is-selected"></i><i class="sw c5"></i><i class="sw c6"></i><i class="sw c7"></i><i class="sw c8"></i></div>

<a class="btn btn-sm" href="#" style="left:186px;top:1213px">ADD TO CART</a>
<a class="btn btn-sm" href="#" style="left:420px;top:1213px">ADD TO CART</a>
<a class="btn btn-sm" href="#" style="left:654px;top:1213px">ADD TO CART</a>
<a class="btn btn-sm" href="#" style="left:888px;top:1213px">ADD TO CART</a>

<!-- product row 2 -->
<div class="product-card" style="left:143px;top:1309px"><div class="product-shot" role="img" aria-label="Hair fibre canister, dark burgundy"></div></div>
<div class="product-card" style="left:377px;top:1309px"><div class="product-shot" role="img" aria-label="Hair fibre canister, rose gold"></div><span class="tag tag-sale2">SALE</span></div>
<div class="product-card" style="left:611px;top:1309px"><div class="product-shot" role="img" aria-label="Hair fibre canister, violet"></div><span class="tag tag-new">NEW</span></div>
<div class="product-card" style="left:846px;top:1309px"><div class="product-shot" role="img" aria-label="Hair fibre canister, pastel rainbow"></div></div>

<div class="product-name" style="left:143px;top:1592px">PRODUCT NAME</div>
<div class="product-name" style="left:377px;top:1592px">PRODUCT NAME</div>
<div class="product-name" style="left:611px;top:1592px">PRODUCT NAME</div>
<div class="product-name" style="left:846px;top:1592px">PRODUCT NAME</div>

<div class="swatches" style="left:143px;top:1629px"><i class="sw c1"></i><i class="sw c2"></i><i class="sw c3"></i><i class="sw c4"></i><i class="sw c5 is-selected"></i><i class="sw c6"></i><i class="sw c7"></i><i class="sw c8"></i></div>
<div class="swatches" style="left:377px;top:1629px"><i class="sw c1"></i><i class="sw c2"></i><i class="sw c3"></i><i class="sw c4"></i><i class="sw c5"></i><i class="sw c6 is-selected"></i><i class="sw c7"></i><i class="sw c8"></i></div>
<div class="swatches" style="left:611px;top:1629px"><i class="sw c1"></i><i class="sw c2"></i><i class="sw c3"></i><i class="sw c4"></i><i class="sw c5"></i><i class="sw c6"></i><i class="sw c7"></i><i class="sw c8 is-selected"></i></div>
<div class="swatches" style="left:846px;top:1629px"><i class="sw c1"></i><i class="sw c2"></i><i class="sw c3"></i><i class="sw c4"></i><i class="sw c5"></i><i class="sw c6"></i><i class="sw c7 is-selected"></i><i class="sw c8"></i></div>

<a class="btn btn-sm" href="#" style="left:186px;top:1676px">ADD TO CART</a>
<a class="btn btn-sm" href="#" style="left:420px;top:1676px">ADD TO CART</a>
<a class="btn btn-sm" href="#" style="left:654px;top:1676px">ADD TO CART</a>
<a class="btn btn-sm" href="#" style="left:888px;top:1676px">ADD TO CART</a>

<!-- colours -->
<div class="colours-band"></div>
<h2 class="colours-title">8 COLOURS</h2>
<p class="colours-text">Lorem ipsum dolor sit amet, consectetur adipiscinged do eiusmod tempor incididunt ut labore et dolore magna aliqua.uis Iuspendisse ultrices gravilsus commodo viverra maecenas accumsan lacus vel facili viverra maecenas accumsan lacsis.</p>
<a class="btn btn-lg" href="#" style="left:145px;top:2030px;width:163px;height:58px">SHOP NOW</a>
<div class="colours-photo" role="img" aria-label="Strip of portraits showing women with eight different vivid hair colours"></div>

<!-- blog -->
<h2 class="section-title" style="top:2229px">FROM THE BLOG</h2>
<div class="blog-city" role="img" aria-label="Dim city skyline at dusk"></div>
<svg class="abs" width="1200" height="200" viewBox="0 0 1200 200" style="left:0;top:2900px">
  <path d="M0 110C120 170 300 200 460 150C620 100 720 30 880 28C1000 26 1100 50 1200 75V200H0Z" fill="#0c1622" opacity="0.55"/>
  <path d="M0 118C120 170 300 195 460 150C620 104 720 32 880 30C1000 28 1100 52 1200 76" fill="none" stroke="var(--accent)" stroke-width="9"/>
</svg>

<div class="blog-grid">
  <article class="blog-card">
    <h3 class="blog-title">AT VERO EOS EACCUSAMU</h3>
    <p class="blog-date">&#9635; Jan 25,2022</p>
    <p class="blog-text">At vero eos et accusamus et iusto odio dignissiducimumos ducimus qui blanditiis pducimuducimuraesentiuAt vero eos et accusamus et iusto odio dignissiducimumos ducimus landitiis pducimuducimurasentiu oluptatum deleniti atque corrupti quos dolores et quas molestias excepturi sint occaecati cupiditate non provident, similique sunt in culpa qui officia deserunt mollitia animi, id est laborum et dolorum fuga. Et harum quidem rerum facilis est et expedita distinctutvolupudiandae.</p>
    <a class="btn btn-sm" href="#">READ MORE</a>
  </article>
  <article class="blog-card is-short">
    <h3 class="blog-title">AT VERO EOS EACCUSAMU</h3>
    <p class="blog-date">&#9635; Jan 25,2022</p>
    <p class="blog-text">At vero eos et accusamus et iusto odio dignissiducimumos ducimus qui blanditiis pducimuducimuraesentiu</p>
    <a class="btn btn-sm" href="#">READ MORE</a>
    <div class="blog-photo" role="img" aria-label="Close view of long blonde and pink hair"></div>
  </article>
  <article class="blog-card">
    <h3 class="blog-title">AT VERO EOS EACCUSAMU</h3>
    <p class="blog-date">&#9635; Jan 25,2022</p>
    <p class="blog-text">At vero eos et accusamus et iusto odio dignissiducimumos ducimus qui blanditiis pducimuducimuraesentiuAt vero eos et accusamus et iusto odio dignissiducimumos ducimus landitiis pducimuducimurasentiu oluptatum deleniti atque corrupti quos dolores et quas molestias excepturi sint occaecati cupiditate non provident, similique sunt in culpa qui officia deserunt mollitia animi, id est laborum et dolorum fuga. Et harum quidem rerum facilis est et expedita distinctutvolupudiandae.</p>
    <a class="btn btn-sm" href="#">READ MORE</a>
  </article>
</div>

<!-- footer -->
<nav class="footer-nav">
  <a href="#">HOME</a><a href="#">ABOUT</a><a href="#">PRODUCTS</a><a href="#">NEWS</a><a href="#">BLOG</a><a href="#">CONTACT</a>
</nav>
<p class="copyright">© 2022 Mille Strand. All rights reserved.Privacy | Terms of Use</p>
<div class="footer-brand">MILLE STRAND</div>
<div class="payments">
  <span class="pay">Paveo</span><span class="pay">Cardora</span><span class="pay">Findal</span><span class="pay">Amblex</span><span class="pay">Palvo</span>
</div>

</body>
</html>
```